Family business needs stationery redesign with new logo

Family owned company, established in 1987 wanting a brand 'refresh'. We are an electrical, refrigeration and construction company based in the Barkly Region Northern Territory, Australia. We have a new logo we would like to use which is uploaded along with our current letterhead and email signature. We are also dropping the word 'contractors' so please do not include this on any designs. Please note also, the 'orange' color used in our logo and designs should be Northern Territory red ochre which is as follows:

RGB (Hex): #C75B12
PantoneĀ® 159 C
CMYK: 1 / 74 / 100 / 7

We are needing our stationery redesigned using our new logo. Please include letterheads, business cards, envelopes, and email signatures.

We currently use our business letterheads for quotations, invoices, letters, HR matters, and internal memos.

We also need a separate simplified letterhead for internal paperwork such as employee leave forms, meeting agendas, and meeting minutes etc.
Updates

Reason: Needing more submissions of full package designs. We are wanting all our stationery, including business cards, letterheads, email signatures, envelopes, etc to be cohesive. We also require ALL the information, as supplied on our template letterhead, to be included on the new letterhead designs. including electrical license no.etc Thank you, K&M

Reason: needing more time as work has got in the way of looking over designs. A lot of designs not meeting the brief/criteria.

Industry/Entity Type

Business

Colors
0355a3
f37122

Requirements
Must have
• The 'orange' color used in the designs should be Northern Territory red ochre which is as follows:
• RGB (Hex): #C75B12
• PantoneĀ® 159 C
• CMYK: 1 / 74 / 100 / 7
• ***MUST INCLUDE ALL INFORMATION THAT IS ON OUR CURRENT LETTERHEAD***
Should not have
• Please do not include the word 'contractors'

```html
<!DOCTYPE html>
<html lang="en">
<head>
<meta charset="utf-8">
<title>K&amp;M Business Card</title>
<link href="https://fonts.googleapis.com/css2?family=Open+Sans:wght@400;600;700&display=swap" rel="stylesheet">
<style>
  :root {
    --navy: #1a3170;
    --ochre: #c75b12;
    --ink: #4a4a4a;
    --rule: #b8b8b8;
    --paper: #ffffff;
    --backdrop: #e4e4e4;
  }
  * { margin: 0; padding: 0; box-sizing: border-box; }
  html, body {
    width: 1200px; height: 987px; overflow: hidden;
    background: var(--backdrop);
    font-family: "Open Sans", sans-serif;
  }
  .canvas { position: relative; width: 1200px; height: 987px; }

  .card {
    position: absolute; left: 293px; width: 616px; height: 352px;
    border-radius: 16px; overflow: hidden;
  }
  .card--front { top: 129px; background: var(--paper); }
  .card--back { top: 505px; background: var(--navy); }

  .wordmark {
    position: absolute; font-weight: 700; line-height: 1; letter-spacing: 1px;
    text-align: center; white-space: nowrap;
  }
  .card--front .wordmark {
    left: 343px; width: 240px; top: 69px; font-size: 74px; color: var(--navy);
  }
  .card--back .wordmark {
    left: 380px; width: 200px; top: 234px; font-size: 56px; color: #fff;
  }

  .edge-tab {
    position: absolute; left: 0; top: 190px; width: 12px; height: 51px;
    background: var(--navy); border-radius: 0 8px 8px 0;
  }

  .holder { position: absolute; left: 42px; top: 196px; }
  .holder__name {
    font-size: 21px; font-weight: 600; color: var(--navy); line-height: 24px;
  }
  .holder__role {
    font-size: 16px; color: var(--ochre); line-height: 20px; text-transform: uppercase;
  }
  .divider {
    position: absolute; left: 42px; top: 245px; width: 535px; height: 1px; background: var(--rule);
  }

  .contacts {
    position: absolute; left: 42px; top: 256px; list-style: none;
    font-size: 16px; color: var(--ink); line-height: 23.5px;
  }
  .contacts li { display: flex; align-items: center; gap: 8px; }
  .contacts svg { width: 16px; height: 14px; fill: var(--navy); flex: none; }

  .address {
    position: absolute; right: 38px; top: 256px; text-align: right;
    font-size: 16px; color: var(--ink); line-height: 23.5px;
  }
  .address__web { color: var(--navy); letter-spacing: 1.5px; }

  .back-web {
    position: absolute; left: 370px; width: 220px; top: 313px; text-align: center;
    font-size: 15px; line-height: 20px; color: #fff; letter-spacing: 1.6px;
  }
</style>
</head>
<body>
<div class="canvas">

  <section class="card card--front">
    <div class="wordmark">K&amp;M</div>
    <div class="edge-tab"></div>
    <div class="holder">
      <p class="holder__name">ALAN BROOKS</p>
      <p class="holder__role">CEO/Founder</p>
    </div>
    <div class="divider"></div>
    <ul class="contacts">
      <li>
        <svg viewBox="0 0 16 16" aria-hidden="true"><path d="M3.5 1l2.6 2.8-1.4 2.1c.9 2 2.5 3.6 4.6 4.6l2.1-1.4L14.2 12l-1.4 2.6C7 14.3 1.7 9 1.4 3.2z"/></svg>
        <span>613 555 0182</span>
      </li>
      <li>
        <svg viewBox="0 0 16 14" aria-hidden="true"><path d="M4 0h8v4H4zM1 5h14v6h-3v3H4v-3H1zM5 9v4h6V9z"/></svg>
        <span>613 555 0194</span>
      </li>
      <li>
        <svg viewBox="0 0 16 12" aria-hidden="true"><path d="M0 0h16v1.5L8 7 0 1.5zM0 3.4l8 5.4 8-5.4V12H0z"/></svg>
        <span>office@kmservices.com</span>
      </li>
    </ul>
    <div class="address">
      <p>12 Wattle Street</p>
      <p>Tennant Creek, NT 0860</p>
      <p class="address__web">www.kmservices.com</p>
    </div>
  </section>

  <section class="card card--back">
    <div class="wordmark">K&amp;M</div>
    <p class="back-web">www.kmservices.com</p>
  </section>

</div>
</body>
</html>
```